Marlowe Tessin Real Estate Business Cards
Professional
Marlowe Tessin
Broker
782 W. Larkspur Ave, Suite 315
Beverly Hills, CA 90210
marlowe@marlowetessinrealestate.com
www.marlowetessinrealestate.com
These comments may or may not be included on the back of the card...
Menu of Services-
Investor Services
1% Listings for Flips
Rehab Management
Auction Services
Bidding
Tax & Title Review
Daily Auction Lists
Property Management Services
Leasing
Maintenance
Evictions
Real Estate Services
Buyers/Sellers
REO Specialists
BPO's
Notary
I'm open to ideas on what to have on either side. I'd like to have my picture and my logo on the card and it may or may not be on the same side. I'm also open to adding comments about services I offer (which I included above) but not sure if it works or not.
EPS Version of the logo
AI Version of the logo
JPG Version of the logo
GIF Version of the logo
My Headshot 1
My Headshot 2

```html
<!DOCTYPE html>
<html lang="en">
<head>
<meta charset="utf-8">
<title>Marlowe Tessin Real Estate – Business Cards</title>
<link href="https://fonts.googleapis.com/css2?family=Source+Sans+3:wght@400;600;700&display=swap" rel="stylesheet">
<style>
  :root {
    --stage: #1d1d1f;
    --teal: #2bb1bf;
    --brown: #7b4b3b;
    --silver-light: #e9eaec;
    --silver-dark: #9a9ca0;
    --paper: #ffffff;
    --ink-brown: #6b3f30;
    --ink-gray: #555a60;
    --white: #ffffff;
  }
  * { box-sizing: border-box; margin: 0; padding: 0; }
  html, body { width: 1200px; height: 969px; overflow: hidden; }
  body {
    background: var(--stage);
    font-family: "Source Sans 3", Arial, sans-serif;
    position: relative;
  }
  .card {
    position: absolute;
    width: 700px;
    height: 400px;
    left: 250px;
    overflow: hidden;
    background: var(--paper);
    box-shadow: 0 6px 18px rgba(0,0,0,.45);
  }
  .card-front { top: 62px; }
  .card-back { top: 507px; }
  .card-art { position: absolute; inset: 0; width: 100%; height: 100%; }

  /* wordmark */
  .wordmark { position: absolute; display: flex; align-items: center; gap: 12px; }
  .wordmark-square { width: 26px; height: 26px; background: var(--teal); flex: none; }
  .wordmark-name {
    font-weight: 600;
    color: var(--ink-brown);
    text-transform: uppercase;
    letter-spacing: 1.5px;
    line-height: 1.05;
  }

  /* front */
  .headshot {
    position: absolute; left: 38px; top: 38px;
    width: 118px; height: 118px; border-radius: 50%;
    border: 4px solid var(--white);
    background: radial-gradient(circle at 50% 40%, #b88b6e 0%, #6e4733 60%, #3d2a22 100%);
  }
  .front-wordmark { left: 270px; top: 84px; }
  .front-wordmark .wordmark-name { font-size: 32px; }
  .agent { position: absolute; left: 38px; top: 174px; color: var(--white); }
  .agent-name { font-size: 20px; font-weight: 700; }
  .agent-title { font-size: 14px; margin-top: 2px; padding-left: 40px; }
  .agent-contact {
    position: absolute; left: 38px; top: 290px;
    color: var(--white); font-size: 12.5px; line-height: 1.45;
    font-style: normal;
  }
  .agent-phone {
    position: absolute; right: 34px; top: 348px;
    color: var(--white); font-size: 19px; letter-spacing: .5px;
  }

  /* back */
  .back-wordmark { left: 380px; top: 44px; }
  .back-wordmark .wordmark-name { font-size: 24px; }
  .website {
    position: absolute; left: 380px; top: 108px;
    color: var(--ink-gray); font-size: 16px; font-weight: 600;
  }
  .services { position: absolute; color: var(--white); }
  .services h3 { font-size: 15px; font-weight: 700; margin-bottom: 3px; }
  .services ul { list-style: none; font-size: 13px; line-height: 1.35; }
  .services li::before { content: "•"; margin-right: 7px; }
  .services-menu { left: 30px; top: 192px; }
  .services-auction { left: 30px; top: 286px; }
  .services-property { left: 262px; top: 286px; }
  .services-realestate { left: 520px; top: 286px; }
</style>
</head>
<body>

<section class="card card-front" aria-label="Business card front">
  <svg class="card-art" viewBox="0 0 700 400" aria-hidden="true">
    <defs>
      <linearGradient id="silverFront" x1="0" y1="0" x2="1" y2="0">
        <stop offset="0" stop-color="var(--silver-dark)"/>
        <stop offset=".5" stop-color="var(--silver-light)"/>
        <stop offset="1" stop-color="var(--silver-dark)"/>
      </linearGradient>
    </defs>
    <rect width="700" height="400" fill="var(--teal)"/>
    <path d="M200 0 H700 V330 C560 296 390 262 200 272 Z" fill="url(#silverFront)"/>
    <path d="M200 0 H700 V306 C560 274 390 240 200 250 Z" fill="var(--paper)"/>
  </svg>
  <div class="headshot" role="img" aria-label="Headshot portrait of Marlowe Tessin"></div>
  <div class="wordmark front-wordmark">
    <span class="wordmark-square"></span>
    <span class="wordmark-name">Marlowe Tessin<br>Real Estate</span>
  </div>
  <div class="agent">
    <p class="agent-name">Marlowe Tessin</p>
    <p class="agent-title">Broker</p>
  </div>
  <address class="agent-contact">
    Marlowe Tessin Real Estate, LLC<br>
    782 W. Larkspur Ave<br>
    Suite 315 Beverly Hills, CA 90210<br>
    marlowe@marlowetessinrealestate.com
  </address>
  <p class="agent-phone">Cell: 310-555-0148</p>
</section>

<section class="card card-back" aria-label="Business card back">
  <svg class="card-art" viewBox="0 0 700 400" aria-hidden="true">
    <defs>
      <linearGradient id="silverBack" x1="0" y1="0" x2="1" y2="0">
        <stop offset="0" stop-color="var(--silver-dark)"/>
        <stop offset=".5" stop-color="var(--silver-light)"/>
        <stop offset="1" stop-color="var(--silver-dark)"/>
      </linearGradient>
    </defs>
    <rect width="700" height="400" fill="var(--brown)"/>
    <path d="M330 0 H700 V160 C520 150 300 160 0 190 V172 C120 120 230 50 330 0 Z" fill="url(#silverBack)"/>
    <path d="M350 0 H700 V140 C520 132 300 140 0 165 V150 C130 102 240 38 350 0 Z" fill="var(--paper)"/>
  </svg>
  <div class="wordmark back-wordmark">
    <span class="wordmark-square"></span>
    <span class="wordmark-name">Marlowe Tessin<br>Real Estate</span>
  </div>
  <p class="website">www.marlowetessinrealestate.com</p>

  <div class="services services-menu">
    <h3>Menu of Services</h3>
    <ul><li>Investor Services</li><li>1% Listings for Flips</li><li>Rehab Management</li></ul>
  </div>
  <div class="services services-auction">
    <h3>Auction Services</h3>
    <ul><li>Bidding</li><li>Tax &amp; Title Review</li><li>Daily Auction Lists</li></ul>
  </div>
  <div class="services services-property">
    <h3>Property Management Services</h3>
    <ul><li>Leasing</li><li>Maintenance</li><li>Evictions</li></ul>
  </div>
  <div class="services services-realestate">
    <h3>Real Estate Services</h3>
    <ul><li>Buyers/Sellers</li><li>REO Specialists</li><li>BPOs</li><li>Notary</li></ul>
  </div>
</section>

</body>
</html>
```